Design business cards for Ironvale Barbers (Opening March so won't need finalised till January2018

Ironvale Barbers is the new age barbers and skincare for all men. Creating tailor made haircuts & customised skincare solutions for the perfect healthy manly look. The Barbers will have a industrial, rustic, worldly feel about it. Rustic red brick wall with old wine barrels as the work stations with the old fashion barber chairs. Concrete floor and a bit corrugated iron around.
Target Market(s)
Professional males who like a great haircut, wet shave and may consider a facial if in the right environment. Total pampering experience in a boys environment.
Industry/Entity Type
Barber
Contact Information for Business Card
Front- Logo - address is 42 Kowhai Rd Taupo
Ph - (07) 548 9163
www.ironvalebarbers.com
email - hello@ironvale.co.nz
Back of card
Mens Haircare - Wet Shaving - Facials - Skin Prescriptions
We are doing a loyalty program - 6 squares numbered then 7th free
Colors
Designer to choose colors to be used in the design.
Requirements
Must have
- Clean simple easy to read.
Nice to have
- Our current colours are white font on black background but thinking we need to introduce another colour. Maybe white logo on a copper, bronze or rusty background. Or even a rustic red brick wall with white writing. Want it clean simple to read. Maybe a burgundy?
Should not have
- no images like heads, scissors, razors please

```html
<!DOCTYPE html>
<html lang="en">
<head>
<meta charset="utf-8">
<title>Ironvale Barbers – Business Card</title>
<link rel="stylesheet" href="https://fonts.googleapis.com/css2?family=Old+Standard+TT:ital,wght@0,400;0,700;1,400&display=swap">
<style>
  :root {
    --stage-light: #cfcfcf;
    --stage-dark: #5a5a5a;
    --card-black: #151516;
    --card-deep: #08080a;
    --gold: #d8b36e;
    --gold-text: #e2c48a;
    --bronze: #a77a3f;
    --silver: #8d8d90;
    --label: #ffffff;
    --box: #ffffff;
    --box-edge: #9a9a9a;
  }
  * { box-sizing: border-box; margin: 0; padding: 0; }
  html, body { width: 1200px; height: 1200px; overflow: hidden; }
  body {
    position: relative;
    background: radial-gradient(circle at 50% 50%, var(--stage-light) 0%, #8f8f8f 45%, var(--stage-dark) 100%);
    font-family: "Old Standard TT", "Times New Roman", serif;
  }
  .side-label {
    position: absolute;
    font-style: italic;
    font-size: 38px;
    color: var(--label);
    line-height: 1;
  }
  .side-label--front { left: 110px; top: 68px; }
  .side-label--back { left: 997px; top: 608px; }

  .card {
    position: absolute;
    width: 680px;
    height: 389px;
    background: var(--card-black);
    overflow: hidden;
  }
  .card--front { left: 87px; top: 126px; }
  .card--back { left: 427px; top: 663px; }

  .card__footer {
    position: absolute;
    left: 0; right: 0; bottom: 0;
    height: 84px;
    background: var(--card-deep);
  }
  .card__ribbon {
    position: absolute;
    left: 0; right: 0;
    height: 70px;
    background: linear-gradient(90deg, #4a4a4d 0%, var(--silver) 25%, #6d5230 48%, var(--bronze) 70%, var(--gold) 85%, #9a6d35 100%);
    opacity: 0.9;
  }
  .card--front .card__ribbon { top: 232px; }
  .card--back .card__ribbon {
    top: 26px;
    background: linear-gradient(90deg, #9a6d35 0%, var(--gold) 18%, var(--bronze) 35%, #6d5230 55%, var(--silver) 75%, #4a4a4d 100%);
  }
  .card--back .card__header {
    position: absolute;
    left: 0; right: 0; top: 0;
    height: 40px;
    background: var(--card-deep);
  }

  .wordmark {
    position: absolute;
    left: 0; right: 0;
    text-align: center;
    color: var(--gold);
    font-weight: 700;
    line-height: 1;
  }
  .wordmark__name { display: block; font-size: 60px; letter-spacing: 1px; }
  .wordmark__sub { display: block; font-size: 22px; letter-spacing: 7px; margin-top: 6px; }
  .card--front .wordmark { top: 84px; }
  .card--back .wordmark { top: 124px; }
  .card--back .wordmark__name { font-size: 54px; }
  .card--back .wordmark__sub { font-size: 20px; margin-top: 2px; }

  .contact {
    position: absolute;
    top: 330px;
    list-style: none;
    color: var(--gold-text);
    font-size: 16.5px;
    line-height: 23px;
  }
  .contact--left { left: 72px; }
  .contact--right { left: 381px; }
  .contact li { display: flex; align-items: center; gap: 8px; }
  .contact svg { width: 14px; height: 14px; flex: none; }

  .services {
    position: absolute;
    top: 219px;
    left: 0; right: 0;
    text-align: center;
    color: var(--gold-text);
    font-size: 22.5px;
  }
  .loyalty {
    position: absolute;
    top: 274px;
    left: 18px;
    display: flex;
    gap: 10px;
  }
  .loyalty__box {
    width: 83px;
    height: 88px;
    background: var(--box);
    border: 3px solid var(--box-edge);
    box-shadow: inset 0 0 0 1px #d8d8d8;
  }
  .loyalty__box--free {
    display: flex;
    flex-direction: column;
    align-items: center;
    justify-content: center;
    color: #000;
    font-weight: 700;
    line-height: 1;
  }
  .loyalty__num { font-size: 44px; }
  .loyalty__num sup { font-size: 24px; vertical-align: 18px; }
  .loyalty__free { font-size: 21px; letter-spacing: 1px; margin-top: 4px; }
</style>
</head>
<body>
  <div class="side-label side-label--front">Front</div>

  <section class="card card--front" aria-label="Front of business card">
    <div class="card__footer"></div>
    <div class="card__ribbon" role="img" aria-label="Flowing gold and silver ribbon decoration"></div>

    <div class="wordmark">
      <span class="wordmark__name">IRONVALE</span>
      <span class="wordmark__sub">BARBERS</span>
    </div>

    <ul class="contact contact--left">
      <li>
        <svg viewBox="0 0 14 14" aria-hidden="true"><path fill="currentColor" d="M7 1 L13 7 H11 V13 H8.5 V9 H5.5 V13 H3 V7 H1 Z"/></svg>
        42 Kowhai Rd Taupo
      </li>
      <li>
        <svg viewBox="0 0 14 14" aria-hidden="true"><path fill="currentColor" d="M3 2 L5 1.5 L6 4.5 L4.8 5.5 C5.4 7.5 6.6 9 8.5 9.8 L9.5 8.6 L12.5 9.6 L12 12 C7 12.5 2.5 8 3 2 Z"/></svg>
        (07) 548 9163
      </li>
    </ul>
    <ul class="contact contact--right">
      <li>
        <svg viewBox="0 0 14 14" aria-hidden="true"><text x="7" y="11" text-anchor="middle" font-size="12" fill="currentColor">@</text></svg>
        www.ironvalebarbers.com
      </li>
      <li>
        <svg viewBox="0 0 14 14" aria-hidden="true"><g fill="none" stroke="currentColor" stroke-width="1.2"><circle cx="7" cy="7" r="5.5"/><ellipse cx="7" cy="7" rx="2.4" ry="5.5"/><path d="M1.5 7 H12.5 M2.5 4.2 H11.5 M2.5 9.8 H11.5"/></g></svg>
        hello@ironvale.co.nz
      </li>
    </ul>
  </section>

  <div class="side-label side-label--back">Back</div>

  <section class="card card--back" aria-label="Back of business card">
    <div class="card__header"></div>
    <div class="card__ribbon" role="img" aria-label="Flowing gold and silver ribbon decoration"></div>

    <div class="wordmark">
      <span class="wordmark__name">IRONVALE</span>
      <span class="wordmark__sub">BARBERS</span>
    </div>

    <p class="services">Mens Haircare - Wet Shaving - Facials - Skin Prescriptions</p>

    <div class="loyalty" aria-label="Loyalty stamps">
      <div class="loyalty__box"></div>
      <div class="loyalty__box"></div>
      <div class="loyalty__box"></div>
      <div class="loyalty__box"></div>
      <div class="loyalty__box"></div>
      <div class="loyalty__box"></div>
      <div class="loyalty__box loyalty__box--free">
        <span class="loyalty__num">7<sup>th</sup></span>
        <span class="loyalty__free">FREE</span>
      </div>
    </div>
  </section>
</body>
</html>
```